Dental office needs a sticker designed for promotions

My dental practice needs a sticker designed to be used on patient bags, promotional items, and give aways like retainer cases. The stickers will be round, 3 inches in diameter. I may have some smaller round stickers printed as will, but will use the same design. The logo should be the primary focus and must use brand colors of red and white. I would like to include our information such as the website (www.ktpvarel.com), phone number (504)631-4098, and social media info - Facebook @varelsmilecare, Instagram @smilecare_at_harbor_varel.

```html
<!DOCTYPE html>
<html lang="en">
<head>
<meta charset="utf-8">
<title>Smilecare at Harbor – Promotional Sticker</title>
<link rel="stylesheet" href="https://fonts.googleapis.com/css2?family=Open+Sans:wght@400;600;700&display=swap">
<style>
  :root {
    --brand-red: #d21f45;
    --leaf-green: #bcd8b1;
    --mist-green: #e4efdf;
    --paper: #ffffff;
  }
  * { margin: 0; padding: 0; box-sizing: border-box; }
  html, body {
    width: 1200px; height: 1200px; overflow: hidden;
    background: var(--paper);
    font-family: "Open Sans", Arial, sans-serif;
    color: var(--brand-red);
  }
  .canvas { position: relative; width: 1200px; height: 1200px; }
  .sticker-art { position: absolute; inset: 0; width: 1200px; height: 1200px; }

  .brand-name {
    position: absolute; left: 237px; width: 720px;
    text-align: center; font-weight: 600; color: var(--brand-red);
    line-height: 1;
  }
  .brand-name__main { top: 350px; font-size: 84px; letter-spacing: 1px; }
  .brand-name__sub  { top: 462px; font-size: 42px; letter-spacing: 3px; }

  .contact {
    position: absolute; left: 237px; width: 720px;
    display: flex; justify-content: center; align-items: center; gap: 8px;
    line-height: 1; white-space: nowrap;
  }
  .contact svg { flex: none; }
  .contact--phone { top: 658px; font-size: 36px; font-weight: 700; }
  .contact--web   { top: 702px; font-size: 36px; font-weight: 700; letter-spacing: 1.5px; }
  .contact--social { font-size: 28px; font-weight: 400; }
  .contact--facebook  { top: 760px; }
  .contact--instagram { top: 804px; }
  .social-square { width: 18px; height: 18px; background: var(--brand-red); border-radius: 3px; flex: none; }
</style>
</head>
<body>
<main class="canvas">
  <svg class="sticker-art" viewBox="0 0 1200 1200">
    <defs>
      <clipPath id="sticker-clip"><circle cx="597" cy="580" r="360"/></clipPath>
      <radialGradient id="green-glow" cx="600" cy="790" r="380" gradientUnits="userSpaceOnUse">
        <stop offset="0" stop-color="#ffffff"/>
        <stop offset="0.45" stop-color="var(--mist-green)"/>
        <stop offset="1" stop-color="var(--leaf-green)"/>
      </radialGradient>
    </defs>
    <circle cx="597" cy="580" r="360" fill="var(--paper)" aria-hidden="true"/>
    <g clip-path="url(#sticker-clip)" role="img" aria-label="Soft green decorative wave band behind the contact details">
      <rect class="green-field" x="230" y="580" width="740" height="380" fill="url(#green-glow)"/>
    </g>
    <circle cx="597" cy="580" r="360" fill="none" stroke="var(--brand-red)" stroke-width="1.6" aria-hidden="true"/>
  </svg>

  <div class="brand-name brand-name__main">Smilecare</div>
  <div class="brand-name brand-name__sub">AT HARBOR</div>

  <div class="contact contact--phone">
    <svg width="22" height="30" viewBox="0 0 22 30" aria-hidden="true">
      <path d="M5 2 L9 2 L10 9 L7 11 C8 16 10 20 13 23 L16 21 L20 25 L18 28 C10 27 3 18 3 6 Z" fill="var(--brand-red)"/>
    </svg>
    <span>(504) 631-4098</span>
  </div>

  <div class="contact contact--web">
    <svg width="28" height="28" viewBox="0 0 28 28" aria-hidden="true" fill="none" stroke="var(--brand-red)" stroke-width="1.8">
      <circle cx="14" cy="14" r="12"/>
      <ellipse cx="14" cy="14" rx="5.5" ry="12"/>
      <line x1="2" y1="14" x2="26" y2="14"/>
      <line x1="4" y1="8" x2="24" y2="8"/>
      <line x1="4" y1="20" x2="24" y2="20"/>
    </svg>
    <span>www.ktpvarel.com</span>
  </div>

  <div class="contact contact--social contact--facebook">
    <span class="social-square"></span>
    <span>@varelsmilecare</span>
  </div>

  <div class="contact contact--social contact--instagram">
    <span class="social-square"></span>
    <span>@smilecare_at_harbor_varel</span>
  </div>
</main>
</body>
</html>
```